Harvesting Victors 6x9 book soft cover- front cover only

We need a book cover for a softcover book. We will need final files in Photoshop or InDesign is preferred.

Overall Title:
Harvesting Victors
Subtitle:
The Foundations of Humble Mentoring for Trainers, Instructors and Players
Author:
by Dr. Marcus Pettiford

The audience is high school and college coaches however we don't want the standard picture with words over the top. Make it a creative design but keep it mind it's a little academic.

```html
<!DOCTYPE html>
<html lang="en">
<head>
<meta charset="utf-8">
<title>Harvesting Victors – Front Cover</title>
<link rel="stylesheet" href="https://fonts.googleapis.com/css2?family=Montserrat:wght@400;500&family=Poppins:wght@500;600&display=swap">
<style>
  :root {
    --ink: #000000;
    --paper: #ffffff;
    --crowd-grey: #8c8c8c;
    --title-blue: #0a1a9c;
    --title-red: #f4151c;
    --accent-blue: #1424d8;
    --accent-gold: #ffd400;
    --trophy-gold: #f7c600;
  }
  html, body {
    margin: 0;
    padding: 0;
    width: 800px;
    height: 1200px;
    overflow: hidden;
    background: var(--paper);
  }
  .cover {
    position: relative;
    width: 800px;
    height: 1200px;
    overflow: hidden;
    background: linear-gradient(to bottom, var(--paper) 0, var(--paper) 500px, var(--ink) 720px, var(--ink) 100%);
  }
  .author {
    position: absolute;
    top: 54px;
    left: 0;
    width: 100%;
    margin: 0;
    text-align: center;
    font-family: "Montserrat", sans-serif;
    font-weight: 400;
    font-size: 44px;
    letter-spacing: 4px;
    color: var(--ink);
  }
  .crowd-art {
    position: absolute;
    left: 0;
    top: 505px;
    width: 800px;
    height: 260px;
    background: linear-gradient(to bottom, rgba(140,140,140,0) 0, var(--crowd-grey) 25%, #3a3a3a 60%, var(--ink) 100%);
  }
  .champion-art {
    position: absolute;
    left: 418px;
    top: 300px;
    width: 150px;
    height: 420px;
    background: linear-gradient(to bottom, var(--trophy-gold) 0, var(--trophy-gold) 18%, #222 30%, var(--ink) 100%);
    border-radius: 70px 70px 0 0;
  }
  .title {
    position: absolute;
    left: 0;
    top: 0;
    margin: 0;
    font-family: "Poppins", sans-serif;
    font-weight: 500;
    text-transform: uppercase;
  }
  .title-line {
    position: absolute;
    display: block;
    white-space: nowrap;
    line-height: 1;
  }
  .title-first {
    left: 52px;
    top: 330px;
    font-size: 62px;
    letter-spacing: -3px;
    color: var(--title-blue);
  }
  .title-second {
    left: 40px;
    top: 390px;
    font-size: 130px;
    letter-spacing: -4px;
    color: var(--title-red);
  }
  .subtitle {
    position: absolute;
    left: 69px;
    top: 862px;
    margin: 0;
    font-family: "Poppins", sans-serif;
    font-weight: 500;
    font-size: 33px;
    line-height: 43px;
    letter-spacing: -1px;
    text-transform: uppercase;
    color: var(--paper);
  }
  .subtitle-line { display: block; white-space: nowrap; }
  .hl-blue { color: var(--accent-blue); }
  .hl-gold { color: var(--accent-gold); }
</style>
</head>
<body>
  <main class="cover">
    <div class="crowd-art" role="img" aria-label="Silhouetted cheering crowd in grey and black"></div>
    <div class="champion-art" role="img" aria-label="Silhouetted athlete raising a gold trophy in celebration"></div>

    <p class="author">DR. MARCUS PETTIFORD</p>

    <h1 class="title">
      <span class="title-line title-first">Harvesting</span>
      <span class="title-line title-second">Victors</span>
    </h1>

    <p class="subtitle">
      <span class="subtitle-line">The Foundations of</span>
      <span class="subtitle-line hl-blue">Humble Mentoring</span>
      <span class="subtitle-line">For <span class="hl-gold">Trainers,</span></span>
      <span class="subtitle-line hl-gold">Instructors and Players</span>
    </p>
  </main>
</body>
</html>
```